ZRM Pty Ltd business card

we need to get a business card designed. We're a large whole seller of baby formula , health supplement and cosmetic products.

Target Market(s)

Big online E commerce platforms, supermarket channels in Asia.

Industry/Entity Type

Business

Contact Information for Business Card

glossy

Logo Text

ZRM

Colors
abd036

Requirements
Must have
• ZRM

```html
<!DOCTYPE html>
<html lang="en">
<head>
<meta charset="utf-8">
<title>ZRM Pty Ltd business card</title>
<link rel="stylesheet" href="https://fonts.googleapis.com/css2?family=Open+Sans:wght@400;600&display=swap">
<style>
  :root {
    --page: #ecebe7;
    --white: #ffffff;
    --paper-grey: #e4e4e4;
    --charcoal: #2d2f30;
    --charcoal-light: #55595b;
    --green: #abd036;
    --green-deep: #4f8a2c;
    --green-mid: #76a83f;
    --silver: #d8dadb;
    --text-light: #e6e8e8;
  }
  * { margin: 0; padding: 0; box-sizing: border-box; }
  html, body { width: 1200px; height: 1023px; overflow: hidden; }
  body {
    background: var(--page);
    font-family: "Open Sans", sans-serif;
    display: flex;
    align-items: center;
    justify-content: center;
    gap: 40px;
  }
  .card {
    position: relative;
    width: 540px;
    height: 310px;
    border-radius: 22px;
    overflow: hidden;
    box-shadow: 0 10px 24px rgba(0,0,0,0.22);
  }
  .card-art { position: absolute; inset: 0; width: 100%; height: 100%; }
  .brand-name {
    position: absolute;
    left: 52px;
    top: 28px;
    font-size: 56px;
    font-weight: 600;
    letter-spacing: 2px;
    color: var(--green);
  }
  .holder {
    position: absolute;
    right: 34px;
    top: 104px;
    text-align: right;
  }
  .holder-name {
    font-size: 18px;
    font-weight: 600;
    color: var(--green);
    text-transform: uppercase;
    letter-spacing: 0.5px;
  }
  .holder-title {
    font-size: 14px;
    color: var(--text-light);
  }
  .contact {
    position: absolute;
    left: 186px;
    bottom: 22px;
    font-size: 13px;
    line-height: 19px;
    color: var(--text-light);
  }
  .contact-address { margin-bottom: 8px; }
  .contact-row { display: flex; align-items: center; gap: 8px; }
  .contact-icon { width: 11px; height: 11px; flex: none; }
  .back-watermark {
    position: absolute;
    left: 36px;
    top: 80px;
    font-size: 130px;
    font-weight: 600;
    color: rgba(255,255,255,0.12);
    letter-spacing: 4px;
    line-height: 1;
  }
  .back-web {
    position: absolute;
    right: 22px;
    top: 34px;
    writing-mode: vertical-rl;
    font-size: 13px;
    letter-spacing: 1.5px;
    color: var(--text-light);
  }
</style>
</head>
<body>

<section class="card card-front" aria-label="Card front">
  <svg class="card-art" viewBox="0 0 540 310" aria-hidden="true">
    <defs>
      <linearGradient id="front-paper" x1="0" y1="0" x2="0" y2="1">
        <stop offset="0" stop-color="#ffffff"/>
        <stop offset="1" stop-color="#e6e6e6"/>
      </linearGradient>
      <linearGradient id="front-dark" x1="0" y1="0" x2="1" y2="1">
        <stop offset="0" stop-color="#5a5e60"/>
        <stop offset="1" stop-color="#242627"/>
      </linearGradient>
      <linearGradient id="front-green" x1="0" y1="1" x2="1" y2="0">
        <stop offset="0" stop-color="#4f8a2c"/>
        <stop offset="0.5" stop-color="#abd036"/>
        <stop offset="1" stop-color="#76a83f"/>
      </linearGradient>
    </defs>
    <rect width="540" height="310" fill="url(#front-paper)"/>
    <path d="M4,310 C100,150 320,60 540,30 L540,46 C320,76 110,165 22,310 Z" fill="#c9cbcc"/>
    <path d="M22,310 C110,165 320,76 540,46 L540,62 C320,92 124,178 44,310 Z" fill="url(#front-green)"/>
    <path d="M44,310 C124,178 320,92 540,62 L540,310 Z" fill="url(#front-dark)"/>
  </svg>
  <div class="brand-name">ZRM</div>
  <div class="holder">
    <div class="holder-name">Daniel Hart</div>
    <div class="holder-title">Managing Director</div>
  </div>
  <div class="contact">
    <div class="contact-address">A-0000 Lindenvale<br>Market Square 000</div>
    <div class="contact-row">
      <svg class="contact-icon" viewBox="0 0 12 12" aria-hidden="true"><path d="M2,1 L4.5,1 L5.5,3.5 L4,4.5 C4.8,6.2 5.8,7.2 7.5,8 L8.5,6.5 L11,7.5 L11,10 C6,10.5 1.5,6 2,1 Z" fill="var(--green)"/></svg>
      <span>000-000-0000</span>
    </div>
    <div class="contact-row">
      <svg class="contact-icon" viewBox="0 0 12 12" aria-hidden="true"><rect x="1" y="2.5" width="10" height="7" rx="1" fill="var(--green)"/><path d="M1.5,3 L6,6.5 L10.5,3" stroke="#2d2f30" stroke-width="1" fill="none"/></svg>
      <span>daniel@zrm.com</span>
    </div>
    <div class="contact-row">
      <svg class="contact-icon" viewBox="0 0 12 12" aria-hidden="true"><circle cx="6" cy="6" r="4.5" fill="none" stroke="var(--green)" stroke-width="1.5"/><path d="M1.5,6 H10.5 M6,1.5 V10.5" stroke="var(--green)" stroke-width="1"/></svg>
      <span>www.zrm.com</span>
    </div>
  </div>
</section>

<section class="card card-back" aria-label="Card back">
  <svg class="card-art" viewBox="0 0 540 310" aria-hidden="true">
    <defs>
      <linearGradient id="back-green" x1="0" y1="0" x2="1" y2="1">
        <stop offset="0" stop-color="#3f7a26"/>
        <stop offset="0.55" stop-color="#6ea53a"/>
        <stop offset="1" stop-color="#4f8a2c"/>
      </linearGradient>
      <linearGradient id="back-dark" x1="0" y1="0" x2="1" y2="0">
        <stop offset="0" stop-color="#2a2c2d"/>
        <stop offset="1" stop-color="#5a5e60"/>
      </linearGradient>
    </defs>
    <rect width="540" height="310" fill="url(#back-green)"/>
    <path d="M372,0 C390,140 440,236 540,292 L540,0 Z" fill="#f1f2f2"/>
    <path d="M384,0 C402,136 450,226 540,276 L540,0 Z" fill="#a9adaf"/>
    <path d="M392,0 C410,132 456,220 540,266 L540,0 Z" fill="url(#back-dark)"/>
  </svg>
  <div class="back-watermark">ZRM</div>
  <div class="back-web">www.zrm.com</div>
</section>

</body>
</html>
```